Visitenkarten-Design für K71.eu - TradeLine Banking
Zielgruppe
Smartphone-Banking mit Mehrwert
Aufgabenstellung
Bitte entwerfen Sie kreative Visitenkarten für uns.
- Halten Sie einen Platz/Rahmen frei für Fotos, die wir nachträglich einsetzen, und kennzeichnen diesen.
- Halten Sie einen Patz/Rahmen für Vor- und Nachname sowie für die Berufsbezeichnung frei und kennzeichnen diesen.
- Halten Sie einen Platz/Rahmen für die Telefonnummern und die Email-Adressen frei und kennzeichnen diesen.
Alle Visitenkarten sollen folgende Daten beinhalten:
Vorname Nachname*
Berufsbezeichnung*
Mobile:
Office:
Email:
Domain:
* = individuell, jeder Mitarbeiter hat eigene Daten
Die Farben müssen sich an unserem CI-Design orientieren, orange/weiß/schwarz/grau -
Außerdem finden Sie unser Logo in der Anlage, welches Sie bitte auf der Karte platzieren.
Bitte liefern Sie uns die Designs in verschiedenen Formaten - psd, ai, eps, jpg, png
Bei Fragen zögern Sie nicht, uns zu kontaktieren. Danke.

```html
<!DOCTYPE html>
<html lang="de">
<head>
<meta charset="utf-8">
<title>K71.eu – Visitenkarten</title>
<link rel="stylesheet" href="https://fonts.googleapis.com/css2?family=Arimo:wght@400;700&display=swap">
<style>
  :root {
    --bg: #e4e4e4;
    --card: #fbfbf9;
    --orange: #e8642a;
    --orange-deep: #d9531c;
    --grey-dark: #4a4a4a;
    --grey-mid: #6b6b6b;
    --white: #ffffff;
  }
  * { box-sizing: border-box; margin: 0; padding: 0; }
  html, body { width: 1200px; height: 900px; overflow: hidden; }
  body {
    background: var(--bg);
    font-family: "Arimo", Arial, sans-serif;
    position: relative;
  }
  .card {
    position: absolute;
    left: 270px;
    width: 660px;
    height: 377px;
    background: var(--card);
    box-shadow: 0 6px 18px rgba(0,0,0,.18);
    overflow: hidden;
  }
  .card--front { top: 48px; }
  .card--back { top: 470px; }

  .brand {
    position: absolute;
    display: flex;
    flex-direction: column;
    align-items: flex-start;
  }
  .brand__row { display: flex; align-items: center; gap: 12px; }
  .brand__square {
    width: 40px; height: 40px;
    background: var(--orange);
  }
  .brand__name {
    font-weight: 700;
    font-size: 52px;
    line-height: 1;
    color: var(--grey-dark);
  }
  .brand__web {
    margin-top: 6px;
    font-weight: 700;
    font-size: 26px;
    color: var(--grey-dark);
    padding-left: 52px;
  }
  .card--front .brand { left: 190px; top: 128px; }
  .card--back .brand { left: 54px; top: 136px; }

  .panel {
    position: absolute;
    top: 0; right: 0;
    width: 320px; height: 100%;
    background: linear-gradient(135deg, var(--orange) 0%, var(--orange-deep) 100%);
  }
  .name-band {
    position: absolute;
    top: 38px; right: 0;
    width: 390px; height: 46px;
    background: var(--grey-mid);
    padding-left: 116px;
    display: flex; align-items: center;
  }
  .name-band__name {
    color: var(--white);
    font-size: 30px;
    font-weight: 400;
  }
  .job-title {
    position: absolute;
    top: 90px; left: 90px;
    color: var(--white);
    font-size: 14px;
    letter-spacing: .5px;
  }
  .address {
    position: absolute;
    top: 112px; left: 90px;
    color: var(--white);
    font-size: 13px;
    line-height: 1.35;
    font-style: normal;
  }
  .contacts {
    position: absolute;
    top: 218px; left: 24px;
    color: var(--white);
    font-size: 16px;
    line-height: 1.3;
    list-style: none;
  }
  .contacts li { display: flex; }
  .contacts dt, .contacts .label { font-weight: 700; width: 76px; }
</style>
</head>
<body>
  <section class="card card--front" aria-label="Vorderseite">
    <div class="brand">
      <div class="brand__row">
        <span class="brand__square"></span>
        <span class="brand__name">K71.eu</span>
      </div>
      <span class="brand__web">www.k71.eu</span>
    </div>
  </section>

  <section class="card card--back" aria-label="Rückseite">
    <div class="brand">
      <div class="brand__row">
        <span class="brand__square"></span>
        <span class="brand__name">K71.eu</span>
      </div>
      <span class="brand__web">www.k71.eu</span>
    </div>

    <div class="panel">
      <div class="job-title">JOB TITLE</div>
      <address class="address">Lindenweg 12<br>84028 Talheim<br>Germany</address>
      <ul class="contacts">
        <li><span class="label">Mobile</span>: +49 170 xxxxxx</li>
        <li><span class="label">Office</span>: +49 871 xxxxxx-xx</li>
        <li><span class="label">Email</span>: yourname@k71.eu</li>
        <li><span class="label">Domain</span>: www.k71.eu</li>
      </ul>
    </div>
    <div class="name-band"><span class="name-band__name">Yourname</span></div>
  </section>
</body>
</html>
```